4Star Hotel looking for web design

Hello everyone,
We are located in Cambodia, the hotel should open in 2-3 months. The name will be Velmora-Boutique Hotel. We are looking for a webdesign which is professional, elegant and SIMPLE.
All informations should be easy to find. We are quite open to proposition but we would like to the home page:
-a carousel with around 5-8 picture
-Little menu where we can book a room
By the way, we would like a page for our restaurant, gallery, contact page for description of the rooms. I add some old pictures.
I give an example of what we are expecting:
www.quenrostays.com/tovelspring
We hope that we are proposing a good job for you guys. Have fun and Thanks.
Oh and the winner ( or someone he had choose) of course have free night in our presidential suite
Target Market(s)
We are looking for european Market. Let s say people middle age who are willing to travel in difficult area
Industry/Entity Type
Hotel
Coding
Coded - Design and coding required
Number of Pages Required
5+ page
Requirements
Must have
- Simple, simple and Simple
- Carousel
- place for book a room
- during booking, a menu for select room , and after that another menu for propose like tour in town, taxi, flower, bottle of champagne for example
- during all the process, the customer should be able to know at what step it is and can stop and come back after
- Have to be perfect for smartphone
- Price with drawbar for they know how much they earn with our reduction
Nice to have
- during the process of information (name, adress, tel...), it would be great if they can fill it with a button facebook, google plus, lindkdin, instagram ....
- then a button share on facebook, twitter for know that they book in our hotel
- At the end of the booking, a flashcode with the recapitulatif that customer can scan.

```html
<!DOCTYPE html>
<html lang="en">
<head>
<meta charset="utf-8">
<title>Velmora-Boutique Hotel — Standard Room</title>
<link rel="stylesheet" href="https://fonts.googleapis.com/css2?family=Open+Sans:wght@400;600;700&family=Oswald:wght@400;500&display=swap">
<style>
:root{
  --brown:#3a1916;
  --brown-2:#4a2420;
  --gold:#f2b134;
  --orange:#f6a82a;
  --page:#e8e5e2;
  --panel:#ffffff;
  --ink:#3c3c3c;
  --muted:#8a8480;
  --line:#dcd8d4;
  --red:#b3302a;
  --star:#e8a21c;
}
*{box-sizing:border-box;margin:0;padding:0}
html,body{width:824px;height:1200px;overflow:hidden}
body{position:relative;background:var(--page);font-family:"Open Sans",sans-serif;color:var(--ink);font-size:8px}
.abs{position:absolute}
h1,h2,h3,.nav a{font-family:"Oswald",sans-serif;font-weight:400;text-transform:uppercase;letter-spacing:.5px}

/* header */
.site-header{left:0;top:0;width:824px;height:70px;background:var(--brown)}
.brand{left:108px;top:0;width:94px;height:80px;background:var(--brown-2);border:1px solid #6a3a33;display:flex;flex-direction:column;align-items:center;justify-content:center;gap:5px;z-index:5}
.brand .mark{width:14px;height:14px;background:var(--gold)}
.brand span{color:#f4e6d0;font-size:8px;font-weight:600;text-align:center;line-height:1.2}
.nav{left:222px;top:38px;display:flex;gap:18px}
.nav a{color:#e9dccb;text-decoration:none;font-size:10px}
.nav a.active{color:var(--gold)}
.topbar{right:104px;top:8px;display:flex;gap:8px;align-items:center;font-size:7px;color:#cbb9a8}
.topbar .btn-book{background:var(--gold);color:var(--brown);padding:2px 6px;font-weight:700}
.topbar .search{width:60px;height:12px;background:#fff;border-radius:2px}

/* hero */
.hero{left:0;top:70px;width:824px;height:170px;background:linear-gradient(100deg,#2b1a16 0%,#5a4030 28%,#3a6f85 55%,#8fc3d4 75%,#2c4e5c 100%)}
.breadcrumb{left:330px;top:78px;width:390px;height:16px;background:rgba(20,10,8,.7);color:#ddd;font-size:7px;padding:4px 8px}
.dropdown{left:226px;top:56px;width:104px;background:#fff;box-shadow:0 2px 4px rgba(0,0,0,.3);z-index:6}
.dropdown li{list-style:none;font-size:8px;padding:5px 8px;border-bottom:1px solid var(--line)}
.dropdown li.current{color:var(--red)}

/* content */
.content{left:96px;top:258px;width:426px;height:692px;background:var(--panel);padding:14px}
.content h1{font-size:15px;color:#333;margin-bottom:10px}
.slider{width:398px;height:180px;background:linear-gradient(135deg,#7a5436,#c9a17a 40%,#e8dcc8 60%,#5c3b27);position:relative}
.slider .arrow{position:absolute;top:82px;width:14px;height:16px;background:rgba(0,0,0,.45)}
.slider .arrow.l{left:0}.slider .arrow.r{right:0}
.dots{display:flex;justify-content:center;gap:4px;margin:8px 0}
.dots i{width:5px;height:5px;border-radius:50%;background:#ccc}
.dots i.on{background:var(--red)}
.content h2{font-size:12px;color:#333;margin:4px 0 6px}
.content p{font-size:7px;line-height:1.6;color:var(--muted)}
.label{font-size:8px;font-weight:700;color:#333;margin:12px 0 6px}
.thumbs{display:flex;gap:9px}
.thumbs div{width:71px;height:70px;border:2px solid #fff;box-shadow:0 0 0 1px var(--line)}
.t1{background:linear-gradient(#6d4a32,#c49a6e)}.t2{background:linear-gradient(#e1d4c2,#8a6746)}
.t3{background:linear-gradient(#bfa27f,#5a3b28)}.t4{background:linear-gradient(#d8c7b0,#7d5b3e)}.t5{background:linear-gradient(#4f3323,#a98462)}
.reviews-tag{display:inline-block;background:var(--red);color:#fff;font-size:7px;padding:2px 6px;margin-top:30px}
.leave{display:block;width:60px;background:#ddd;font-size:7px;padding:3px 6px;margin:6px 0 10px;text-align:center;color:#555}
.review{border-top:1px solid var(--line);padding:6px 0}
.review .meta{display:flex;gap:6px;align-items:center;font-size:7px;color:var(--muted)}
.stars{color:var(--star);font-size:8px;letter-spacing:1px}
.review .body{margin-top:4px;background:#eeeeec;height:22px;font-size:7px;padding:6px;color:#666}

/* sidebar */
.sidebar{left:540px;top:258px;width:180px;height:300px;background:var(--panel);padding:12px}
.sidebar h3{font-size:10px;color:#333;margin-bottom:8px}
.sidebar li{list-style:none;font-size:7px;color:var(--muted);padding:3px 0 3px 10px;position:relative}
.sidebar li::before{content:"";position:absolute;left:0;top:6px;width:4px;height:4px;background:var(--gold)}
.booking-card{left:540px;top:430px;width:180px;height:90px;background:var(--panel);padding:10px;display:flex;gap:8px}
.booking-card .pic{width:70px;height:60px;background:linear-gradient(#8a6a4c,#d3b999)}
.booking-card h3{font-size:9px;color:var(--red)}
.booking-card p{font-size:6.5px;color:var(--muted);line-height:1.5}

/* booking form */
.booking-form{left:490px;top:508px;width:310px;height:192px;background:var(--orange);padding:10px 14px;box-shadow:0 3px 8px rgba(0,0,0,.25);z-index:4}
.booking-form .lead{font-size:8px;color:#4a2a10;font-weight:600;margin-bottom:8px}
.row{display:flex;justify-content:space-between;align-items:center;margin-bottom:7px;font-size:7px;color:#3d2208}
.field{background:#fff;height:12px;border:1px solid #d78d1a}
.price{font-family:"Oswald",sans-serif;font-size:12px;color:#3d2208}
.price s{font-size:9px;color:#7a4a15;margin-right:4px}
.submit{position:absolute;right:14px;bottom:10px;background:var(--red);color:#fff;font-size:7px;padding:3px 10px}

/* footer */
.site-footer{left:0;top:968px;width:824px;height:232px;background:var(--brown);color:#d8c7b4}
.site-footer h3{font-size:10px;color:#f0e2cf;margin-bottom:8px}
.f-col p{font-size:7px;line-height:1.6;color:#b9a593}
.post{display:flex;gap:6px;margin-bottom:8px}
.post .pic{width:30px;height:26px;background:linear-gradient(#6b4b34,#b28c66);flex:none}
.post b{display:block;font-size:7px;color:var(--gold)}
.widget{background:#fff;padding:6px}
.widget .cover{height:40px;background:linear-gradient(#6b7b5a,#a89070)}
.widget .name{display:flex;align-items:center;gap:4px;font-size:7px;font-weight:700;color:#333;margin:5px 0}
.widget .name i{width:8px;height:8px;background:var(--brown)}
.widget .grid{display:flex;flex-wrap:wrap;gap:3px}
.widget .grid i{width:18px;height:14px;background:#c9b39a}
.social{left:0;top:1142px;width:824px;display:flex;justify-content:center;gap:6px}
.social i{width:16px;height:16px;background:#6e4640}
.copy{left:0;top:1178px;width:824px;text-align:center;font-size:7px;color:#a38f7e}
</style>
</head>
<body>

<header class="site-header abs"></header>
<div class="brand abs"><div class="mark"></div><span>Velmora-Boutique<br>Hotel</span></div>
<nav class="nav abs">
  <a href="#">Home</a><a class="active" href="#">Accommodation</a><a href="#">Restaurant &amp; Bar</a><a href="#">Meeting &amp; Events</a><a href="#">Blog</a>
</nav>
<div class="topbar abs"><span class="btn-book">Booking</span><span>Contact Us</span><span>Gallery</span><span>Location</span><span class="search"></span></div>

<div class="hero abs" role="img" aria-label="Hotel pool and terrace overlooking the river"></div>
<div class="breadcrumb abs">Home / Accommodation / Standard Room — from $45 per night</div>
<ul class="dropdown abs">
  <li>Deluxe room</li><li class="current">Standard Room</li><li>Family Suite</li><li>Junior Suite</li><li>Suite</li>
</ul>

<main class="content abs">
  <h1>Standard Room</h1>
  <div class="slider" role="img" aria-label="Standard room with double bed and wooden furniture"><span class="arrow l"></span><span class="arrow r"></span></div>
  <div class="dots"><i class="on"></i><i></i><i></i><i></i><i></i></div>
  <h2>About Room</h2>
  <p>Our standard rooms offer a calm retreat with handcrafted wooden furniture, a comfortable double bed, air conditioning, free wifi and a private bathroom with rain shower. Large windows open onto the garden, and every stay includes breakfast served on our terrace each morning.</p>
  <div class="label">Gallery</div>
  <div class="thumbs">
    <div class="t1" role="img" aria-label="Room interior"></div>
    <div class="t2" role="img" aria-label="Bathroom"></div>
    <div class="t3" role="img" aria-label="Bedroom detail"></div>
    <div class="t4" role="img" aria-label="Seating corner"></div>
    <div class="t5" role="img" aria-label="Balcony view"></div>
  </div>
  <span class="reviews-tag">Reviews</span>
  <span class="leave">Leave review</span>
  <div class="review"><div class="meta"><span>Average rating</span><span class="stars">★★★★★</span></div></div>
  <div class="review"><div class="meta"><span class="stars">★★★★★</span><span>Aug 20, 2013 by Marie Roux</span></div><div class="body">Great room, friendly staff and a quiet garden.</div></div>
  <div class="review"><div class="meta"><span class="stars">★★★★☆</span><span>Jul 14, 2013 by Jonas Weber</span></div><div class="body">Clean and comfortable, perfect base for the region.</div></div>
  <div class="review"><div class="meta"><span class="stars">★★★★★</span><span>Jun 02, 2013 by Elena Sorli</span></div><div class="body">Wonderful breakfast and very helpful team.</div></div>
</main>

<aside class="sidebar abs">
  <h3>Amenities &amp; Services</h3>
  <ul>
    <li>24-hour front desk</li><li>Free wifi in all rooms and lobby</li><li>Outdoor swimming pool</li><li>Airport transfer on request</li>
    <li>Air conditioning</li><li>Daily housekeeping</li><li>Tours and travel desk</li><li>Laundry service</li>
  </ul>
</aside>
<div class="booking-card abs">
  <div class="pic" role="img" aria-label="Hotel entrance"></div>
  <div><h3>Booking</h3><p>Reserve online and save on our best available rate.</p></div>
</div>

<form class="booking-form abs">
  <div class="lead">Fill out the form below and book your room today</div>
  <div class="row"><span>Room 1</span><span class="price"><s>$60</s>$45</span></div>
  <div class="row"><span>Adults</span><span class="field" style="width:60px"></span><span>Children</span><span class="field" style="width:60px"></span></div>
  <div class="row"><span>Check in</span><span class="field" style="width:80px"></span><span>Check out</span><span class="field" style="width:80px"></span></div>
  <div class="row"><span>Name</span><span class="field" style="width:220px"></span></div>
  <div class="row"><span>Email</span><span class="field" style="width:220px"></span></div>
  <div class="row"><span>Phone</span><span class="field" style="width:220px"></span></div>
  <span class="submit">Submit</span>
</form>

<footer class="site-footer abs">
  <div class="f-col abs" style="left:96px;top:20px;width:200px">
    <h3>About Our Hotel</h3>
    <p>A small boutique hotel in the green highlands of Cambodia, close to waterfalls, crater lakes and village markets. We welcome travellers who seek comfort after a day of adventure, with warm service and local flavours.</p>
  </div>
  <div class="f-col abs" style="left:320px;top:20px;width:200px">
    <h3>From Our Blog</h3>
    <div class="post"><div class="pic"></div><div><b>22.08.2013</b><p>Opening season news and first guest impressions.</p></div></div>
    <div class="post"><div class="pic"></div><div><b>10.08.2013</b><p>Five day trips to enjoy around the province.</p></div></div>
  </div>
  <div class="widget abs" style="left:540px;top:20px;width:180px">
    <div class="cover"></div>
    <div class="name"><i></i>Velmora-Boutique Hotel</div>
    <div class="grid"><i></i><i></i><i></i><i></i><i></i><i></i><i></i><i></i><i></i><i></i><i></i><i></i><i></i><i></i></div>
  </div>
</footer>
<div class="social abs"><i></i><i></i><i></i><i></i><i></i></div>
<div class="copy abs">Copyright © 2013, Velmora-Boutique Hotel. All Rights Reserved.</div>

</body>
</html>
```